Events & Entertainment Production Coordination Business Cards

We need a business card for a new company based in Los Angeles called "Bright Harbor Works"
Our company brings people together for events and helps coordinate different productions. We bring artists from a different country to perform or do events in the U.S.
We are looking for something fun, lively, colorful, creative, and simple.
Nothing that looks too crisp, dark, stiff, or modern.
We connect people from different parts of the world, so definitely something eye-catching will be great!
Colors we would like to see are Black, Yellow, Red, White, Brown to name a few. (Feel free to use more!)
(Double-sided is an option also)
Business
Contact Information for Business Card
Contact Information to put on Business Card:
Name
Title
Address - 2 lines
Phone - place for 3 numbers
E-mail
URL

```html
<!DOCTYPE html>
<html lang="en">
<head>
<meta charset="utf-8">
<title>Bright Harbor Works — Business Card</title>
<link href="https://fonts.googleapis.com/css2?family=Open+Sans:wght@400;600;700&display=swap" rel="stylesheet">
<style>
  :root {
    --backdrop: #2a2a2a;
    --card: #050505;
    --orange: #f26522;
    --amber: #f7941d;
    --white: #ffffff;
  }
  * { margin: 0; padding: 0; box-sizing: border-box; }
  html, body {
    width: 1200px; height: 900px; overflow: hidden;
    background: var(--backdrop);
    font-family: "Open Sans", Arial, sans-serif;
  }
  .stage { position: relative; width: 1200px; height: 900px; }
  .card {
    position: absolute;
    width: 560px; height: 320px;
    background: var(--card);
    border-radius: 22px;
    box-shadow: 0 14px 30px rgba(0,0,0,0.55);
    overflow: hidden;
  }
  .card--front { left: 70px; top: 100px; }
  .card--back { left: 570px; top: 480px; }

  .brand-dot {
    display: block; flex: none;
    border-radius: 50%;
    background: var(--amber);
  }

  /* front: large centred brand */
  .front-brand {
    position: absolute; inset: 0;
    display: flex; align-items: center; justify-content: center; gap: 20px;
  }
  .front-brand .brand-dot { width: 120px; height: 120px; }
  .front-brand .brand-name {
    color: var(--orange); font-weight: 700; font-size: 36px; line-height: 1.1;
  }

  /* back */
  .back-brand {
    position: absolute; left: 34px; top: 92px;
    display: flex; align-items: center; gap: 12px;
  }
  .back-brand .brand-dot { width: 46px; height: 46px; }
  .back-brand .brand-name {
    color: var(--orange); font-weight: 700; font-size: 25px;
  }
  .divider {
    position: absolute; left: 34px; width: 406px; top: 196px;
    height: 2px; background: var(--orange);
  }
  .person-name {
    position: absolute; right: 120px; top: 166px;
    color: var(--orange); font-weight: 700; font-size: 20px; letter-spacing: 0.3px;
    line-height: 1;
  }
  .person-title {
    position: absolute; left: 446px; top: 188px;
    color: var(--white); font-size: 11px; letter-spacing: 0.8px; line-height: 1;
  }
  .address {
    position: absolute; right: 34px; top: 224px; text-align: right;
    font-style: normal;
    color: var(--white); font-size: 12.5px; line-height: 1.45;
  }
  .contacts {
    position: absolute; left: 34px; top: 206px; list-style: none;
    color: var(--white); font-size: 13px; line-height: 1.3;
  }
  .contacts li { display: flex; align-items: center; gap: 9px; }
  .contacts svg { width: 11px; height: 11px; flex: none; fill: var(--orange); }
</style>
</head>
<body>
<main class="stage">

  <section class="card card--front" aria-label="Card front">
    <div class="front-brand">
      <span class="brand-dot"></span>
      <span class="brand-name">Bright Harbor Works</span>
    </div>
  </section>

  <section class="card card--back" aria-label="Card back">
    <div class="back-brand">
      <span class="brand-dot"></span>
      <span class="brand-name">Bright Harbor Works</span>
    </div>

    <p class="person-name">DANA REYES</p>
    <div class="divider"></div>
    <p class="person-title">DIRECTOR</p>

    <address class="address">
      14 - 20 Marlow Lane St<br>
      Westvale Bay 2207 California
    </address>

    <ul class="contacts">
      <li>
        <svg viewBox="0 0 24 24"><path d="M6.6 10.8a15 15 0 0 0 6.6 6.6l2.2-2.2c.3-.3.7-.4 1-.2 1.1.4 2.3.6 3.6.6.6 0 1 .4 1 1V20c0 .6-.4 1-1 1A17 17 0 0 1 3 4c0-.6.4-1 1-1h3.5c.6 0 1 .4 1 1 0 1.3.2 2.5.6 3.6.1.3 0 .7-.2 1z"/></svg>
        +310 4182-7735
      </li>
      <li>
        <svg viewBox="0 0 24 24"><path d="M7 1h10a2 2 0 0 1 2 2v18a2 2 0 0 1-2 2H7a2 2 0 0 1-2-2V3a2 2 0 0 1 2-2zm0 3v14h10V4zm5 15.5a1 1 0 1 0 0 2 1 1 0 0 0 0-2z"/></svg>
        +310 5527-9014
      </li>
      <li>
        <svg viewBox="0 0 24 24"><path d="M6 2h9l3 3v5H6zM4 11h16a2 2 0 0 1 2 2v7a2 2 0 0 1-2 2H4a2 2 0 0 1-2-2v-7a2 2 0 0 1 2-2zm3 3v2h4v-2z"/></svg>
        +310 6203-4486
      </li>
      <li>
        <svg viewBox="0 0 24 24"><path d="M2 5h20v14H2zm2 2v.5l8 5 8-5V7zm0 3v7h16v-7l-8 5z"/></svg>
        info@brightharborworks.com
      </li>
      <li>
        <svg viewBox="0 0 24 24"><path d="M12 2a10 10 0 1 0 0 20 10 10 0 0 0 0-20zm6.9 6h-3a15 15 0 0 0-1.3-3.9A8 8 0 0 1 18.9 8zM12 4c.8 1.1 1.5 2.5 1.9 4h-3.8c.4-1.5 1.1-2.9 1.9-4zM4.3 14a8 8 0 0 1 0-4h3.4a16 16 0 0 0 0 4zm.8 2h3a15 15 0 0 0 1.3 3.9A8 8 0 0 1 5.1 16zm3-8h-3a8 8 0 0 1 4.3-3.9C8.8 5.3 8.4 6.6 8.1 8zM12 20c-.8-1.1-1.5-2.5-1.9-4h3.8c-.4 1.5-1.1 2.9-1.9 4zm2.3-6H9.7a14 14 0 0 1 0-4h4.6a14 14 0 0 1 0 4zm.3 5.9c.6-1.2 1-2.5 1.3-3.9h3a8 8 0 0 1-4.3 3.9zm1.7-5.9a16 16 0 0 0 0-4h3.4a8 8 0 0 1 0 4z"/></svg>
        www.brightharborworks.com
      </li>
    </ul>
  </section>

</main>
</body>
</html>
```